Design Fresh and modern brochure about hypnosis

We need a clean and modern brochure designed for our hypnosis center. I have text, a logo, and a single image. I'd like all placed in a tri-fold brochure with design elements added and I'd like the result in a format which can be modified, like InDesign. The brochure should appear modern and clean, but also with a softer look to appear compassionate. The company values are professional, compassionate, and local. Local is the Pacific Northwest. Colors should match the logo, blue with elements of water. I'd like to see shades of blue with white.
Updates

Hello designers. Thank you all for your great brochure designs thus far. 

At this time I've narrowed down the top 2 designs and those designers have been contacted. 

So right now, any new designs would be in consideration for third place. I want to be fair to your time, so please consider if you're still interested in submitting a design for 3rd place or not. 

Thank you. 

Target Market(s)

Adults in western US who want to improve their lives. Primarily 30+ in age, english speaking, and working full or part time.

Industry/Entity Type

It Company

Colors
85cae6
0555a3
3276b5
86cfc6
32b7a4

Requirements
Must have
• The brochure must include the logo and image attached, and should fit in the tri-fold design, similar to the example brochure. It also needs to be in a format that can be easily modified over time, as I typically change text in the brochure. InDesign would be great.
Nice to have
• Additional design elements - like areas for a call-out to highlight features.

```html
<!DOCTYPE html>
<html lang="en">
<head>
<meta charset="utf-8">
<title>Tidewater Hypnosis Center – Tri-fold Brochure</title>
<link href="https://fonts.googleapis.com/css2?family=Lora:wght@400;700&family=PT+Sans:wght@400;700&display=swap" rel="stylesheet">
<style>
  :root {
    --backdrop: #e6e7e8;
    --paper: #ffffff;
    --ink: #2a2a2a;
    --navy: #0b3f73;
    --blue-deep: #0555a3;
    --blue-mid: #3276b5;
    --blue-sky: #85cae6;
    --teal-soft: #86cfc6;
    --teal: #32b7a4;
    --accent-red: #a3262a;
    --white: #ffffff;
  }
  * { box-sizing: border-box; margin: 0; padding: 0; }
  html, body { width: 1200px; height: 540px; overflow: hidden; }
  body { background: var(--backdrop); position: relative; font-family: "PT Sans", sans-serif; }

  .sheet { position: absolute; display: flex; background: var(--paper); box-shadow: 0 2px 6px rgba(0,0,0,.18); }
  .sheet--inside { left: 52px; top: 95px; width: 532px; height: 350px; }
  .sheet--outside { left: 622px; top: 100px; width: 525px; height: 340px; }

  .panel { position: relative; height: 100%; overflow: hidden; }

  /* Inside sheet */
  .sheet--inside .panel { font-family: "Lora", serif; font-size: 7.1px; line-height: 9.6px; color: var(--ink); }
  .panel--intro { width: 193px; padding: 14px 14px 0 12px; }
  .sheet--inside .panel--therapy { width: 173px; padding: 4px 12px 0 12px; color: var(--white);
    font-size: 6.9px; line-height: 9px;
    background: linear-gradient(160deg, #2fa6e6 0%, #1b8fd6 45%, #3aa9e8 100%); }
  .sheet--inside .panel--session { width: 166px; padding: 14px 12px 0 12px; font-size: 7.5px; line-height: 11.1px; }
  .panel-heading { font-family: "Lora", serif; font-weight: 700; font-size: 11.5px; line-height: 14px; margin: 2px 0 6px; color: #111; }
  .panel--therapy .panel-heading { color: var(--white); font-size: 11.5px; margin: 8px 0 5px; }
  .marker { position: absolute; left: 0; width: 3px; background: var(--accent-red); }
  .panel--intro .marker { top: 13px; height: 18px; }
  .panel--session .marker { top: 13px; height: 22px; }
  .web-line { position: absolute; bottom: 6px; left: 0; right: 0; text-align: center; font-size: 5.5px; line-height: 7px; opacity: .85; }

  /* Outside sheet */
  .panel--success { width: 163px; padding: 16px 11px 0 11px; color: var(--white); font-size: 6.6px; line-height: 9.9px;
    background: linear-gradient(150deg, #0a6fc4 0%, #1c8fdb 55%, #57b6ea 100%); }
  .success-heading { font-weight: 700; font-size: 8.6px; line-height: 10.5px; margin-bottom: 3px; }
  .panel--services { width: 198px; padding: 10px 12px 0 14px; color: var(--ink); }
  .services-heading { font-weight: 700; font-size: 9.2px; line-height: 11px; margin-bottom: 6px; }
  .services-list { display: grid; grid-template-columns: 1fr 1fr; column-gap: 4px; font-size: 6.2px; line-height: 10px; }
  .contact-callout { margin-top: 14px; text-align: center; font-weight: 700; font-size: 8.8px; line-height: 10.5px; }
  .portrait { display: block; width: 80px; height: 84px; margin: 8px auto 4px; background: linear-gradient(180deg, #9fb4c2 0%, #7d8d86 55%, #5e6b5e 100%); }
  .contact-details { text-align: center; font-weight: 700; font-size: 8.6px; line-height: 10.4px; }
  .panel--cover { width: 164px; padding: 16px 10px 0 10px; text-align: center; color: var(--navy);
    background: linear-gradient(160deg, #a9d7ee 0%, #c4e4f4 45%, #e6f4fb 100%); }
  .cover-title { font-size: 13.5px; line-height: 16.5px; font-weight: 400; }
  .cover-rule { border: none; border-top: 1px solid var(--navy); margin: 8px 4px 8px; }
  .cover-tagline { font-weight: 700; font-size: 14.5px; line-height: 18px; }
  .brand { position: absolute; left: 0; right: 0; top: 236px; text-align: center; }
  .brand-mark { display: block; width: 30px; height: 30px; margin: 0 auto 6px; border-radius: 50%; background: var(--blue-mid); }
  .brand-name { font-family: "PT Sans", sans-serif; font-size: 12px; line-height: 14px; letter-spacing: 1.5px; text-transform: uppercase; color: var(--blue-mid); }
</style>
</head>
<body>

<section class="sheet sheet--inside">
  <article class="panel panel--intro">
    <span class="marker"></span>
    <h2 class="panel-heading">What is hypnosis?</h2>
    <p>Hypnosis is a state of focused consciousness. Your hypnotherapist will assist you in learning how to achieve this state by guiding you into it. Once this has been achieved, you will then receive what are called hypnotic suggestions. These suggestions will enable you to use the power of hypnosis in your life and make the changes you desire.</p>
    <p>Hypnosis is a tool that can help you just, like it has helped millions of other people to take back control of their lives.</p>
    <p>Hypnosis can help you change old habits and to provide you with motivation to do the things that you may have been putting off.</p>
    <p>Hypnosis has been sanctioned and used by the medical community since 1958 to help patients overcome chronic pain, create anesthesia, and heal psychogenic illnesses.</p>
    <p>Hypnosis and self-hypnosis have been shown to be effective in reducing stress and stress-related illnesses.</p>
    <p>Hypnosis has also been shown to help mothers give birth to their children with little or no pain.</p>
    <h2 class="panel-heading" style="margin-top:8px">Is hypnosis safe?</h2>
    <p>Hypnosis is safe. It is very similar to experiencing a daydream. Usually you will feel relaxed when doing hypnosis.</p>
    <p>Hypnosis in and of itself is a very pleasant experience. It is a time to let go of the other thoughts of the day and focus on the issues you came in to work on.</p>
  </article>

  <article class="panel panel--therapy">
    <p>Scientist, medical professionals, psychologists and hypnotherapists have been using hypnosis for over 200 years and no one has ever been hurt by simply going into hypnosis.</p>
    <h2 class="panel-heading">What is hypnotherapy?</h2>
    <p>Hypnotherapy is the applied use of hypnosis. Therapy can be defined as anything that is done to move someone toward health and wholeness. Thus, hypnotherapy is the use of hypnosis to help you move toward health and wholeness.</p>
    <p>Hypnotherapy is also used to help you reach goals when nothing else has helped. See the back panel of this brochure to see a list of uses for hypnotherapy.</p>
    <p>Self-hypnosis may also be part of a good hypnotherapy program. Ask your hypnotherapist if using self-hypnosis is recommended to help you reach your goals.</p>
    <p>Can I be hypnotized?</p>
    <p>Of course you can! You already have been. It's easy to go into hypnosis and it is a normal state of mind that everyone has already experienced.</p>
    <p>In fact, hypnosis is such a normal state of mind, most people usually don't even realize that they are hypnotized.</p>
    <p>Normal, everyday hypnosis occurs when you are driving down the road and lose track of time, or, when you are focusing on a book or television program and you don't even notice something that is going on around you.</p>
    <span class="web-line">www.TidewaterHypnosisCenter.com</span>
  </article>

  <article class="panel panel--session">
    <span class="marker"></span>
    <p>When you come in for hypnosis, all you need to do is to be able to follow the instructions of the hypnotherapist and you can put the power of hypnosis to work for you.</p>
    <p>Anyone of with the willingness and ability to follow instructions can experience hypnosis and use it to improve his or her life. This includes children and teenagers.</p>
    <p>Who will hypnotize me?</p>
    <p>Your hypnotist or hypnotherapist is a highly qualified professional. He or she is certified and registered with the Regional Council of Hypnotists.</p>
    <p>Your hypnotherapist is bound by professional ethics and the laws of the state in which it is practiced.</p>
    <p>In addition, your hypnotherapist has achieved extra certification in the advanced hypnotherapy system called Pathway. Rest assured that he or she will treat you with respect, and that your visits are completely confidential.</p>
    <p>We suggest that you call and speak to us directly so that you can learn more about hypnosis and hypnotherapy. This will allow you to become more familiar with</p>
  </article>
</section>

<section class="sheet sheet--outside">
  <article class="panel panel--success">
    <h2 class="success-heading">Hypnosis can help you succeed when nothing else has worked!</h2>
    <p>Hypnosis is one of the fastest growing fields of human achievement. As hypnotherapists we are working with people who are frustrated because nothing else has helped them achieve their goals.</p>
    <p>They have tried every other avenue that they can think of without success. We use hypnosis, hypnotherapy and teach self-hypnosis so that people like you can succeed in making important changes.</p>
    <p>Did you know that many of the most successful professional and Olympic teams use hypnosis to help their athletes win? That's true.</p>
    <p>Now you can use this advantage for yourself, whether you are trying to overcome an old problem or if you want to grow to a new level of personal achievement.</p>
    <p>Hypnotherapy can also be used as a complementary treatment for some medical and psychological issues. We can contact your doctor to make sure that using hypnosis is appropriate for your situation.</p>
    <p>Appropriate issues may include pain management, stress related illness and any issue that has been labeled psychogenic in origin. Hypnosis can be your tool for success!</p>
    <p>We encourage you to call or come into our office and ask us questions about hypnosis and our services. We enjoy answering questions. It is part of our job.</p>
  </article>

  <article class="panel panel--services">
    <h2 class="services-heading">Hypnosis can help you with the following and more:</h2>
    <div class="services-list">
      <span>Stop Smoking&nbsp; Weight Loss</span><span>Issues&nbsp; Sexual Issues Abuse</span>
      <span>Anxiety&nbsp; Stress Remove</span><span>Issues&nbsp; Self-Esteem</span>
      <span>Fears&nbsp; Relationships Remove</span><span>Concentration</span>
      <span>Habits&nbsp; Alcohol Abuse Drug</span><span>Self-Confidence Test Anxiety</span>
      <span>Abuse&nbsp; Childbirth</span><span>Shyness Procrastination</span>
      <span>Motivation&nbsp; Stage Fright</span><span>Improve Mood Improve</span>
      <span>Public Speaking</span><span>Sports&nbsp; Children's Issues</span>
      <span>Pain Management Anger</span><span>And, More…</span>
    </div>
    <p class="contact-callout">Contact our office for more information. Your hypnotherapist will be happy to tell you about appointment availability and fees for services.</p>
    <div class="portrait" role="img" aria-label="Portrait photo of the hypnotherapist outdoors"></div>
    <div class="contact-details">
      <p>(360) 555-0147</p>
      <p>TidewaterHypnosisCenter.com</p>
      <p>Copyright © 2014 Tidewater Hypnosis Center. All rights reserved.</p>
      <p>TidewaterHypnosisCenter.com</p>
    </div>
  </article>

  <article class="panel panel--cover">
    <h1 class="cover-title">Hypnosis<br>and<br>Hypnotherapy<br>Information</h1>
    <hr class="cover-rule">
    <p class="cover-tagline">Learn how hypnosis and hypnotherapy can help you succeed.</p>
    <div class="brand">
      <span class="brand-mark"></span>
      <span class="brand-name">Tidewater<br>Hypnosis Center</span>
    </div>
  </article>
</section>

</body>
</html>
```